Booklet Design needed for Brightfold Web Studio

A Little bit about us:
At Brightfold Web Studio we offer our clients the very best in their website needs without the big price tag.

We take the hassle out of setting up a website and take care of the website design, domain registration, SEO and hosting.
We know how important it is to have a Visually Appealing website, that’s why when we are designing our websites we focus on the main things like branding, content, creativity, colors, layout, ease of use, and imagery.

Design Specifics:
I currently have two booklets that I give to my clients:
one before I start designing their site as a general information booklet
and the other one I give only once I complete their site - which is about how to use my editor.

I want to jazz these two booklets up and bit with a modern and professional look, and I want both the booklets to have a similar design, I would also like it to be a similar look to my website, www.brightfoldwebstudio.com.au.

Previously the budget was AUD$130. Now it is AUD$260.
This reflects your creative effort for 2 booklets.

I have uploaded the two booklets, labeled Booklet 1 (7 pages) and Booklet 2 (15 pages), inside you will find the information and images I want on each page.
The booklets also need a title page.

Thanks Designers. Will appreciate all your creative effort!

Hi Designers . i have updated the content for one of the booklets. the new file which i will upload shortly is called "New Client information Booklet content update". please use this for one of the booklets to be designed. the other booklet still needs to be done (the one with the editor information inside)Cheers Added Thursday, October 29, 2015

Target Market(s)

Small to medium Businesses

Font styles to use
Sans Serif

Colors
3176b5
5c5c5c
ffffff

Requirements
Must have
• Logo, images and content from original booklets. And the Seperate booklets for the two different booklets. Similar modern, professional design.
Nice to have
• Moder, professional design, similar look to my website. Www.brightfoldwebstudio.com.au

```html
<!DOCTYPE html>
<html lang="en">
<head>
<meta charset="utf-8">
<title>Brightfold Web Studio – Welcome</title>
<link href="https://fonts.googleapis.com/css2?family=Alegreya+Sans:wght@300;400;500;700&display=swap" rel="stylesheet">
<style>
  :root {
    --brand-blue: #2f6fb2;
    --brand-grey: #4d4d4d;
    --body-grey: #3a3a3a;
    --muted-grey: #8a8a8a;
    --bullet-grey: #4a4a4a;
    --band-dark: #1c2530;
    --white: #ffffff;
  }
  * { margin: 0; padding: 0; box-sizing: border-box; }
  html, body { width: 928px; height: 1200px; overflow: hidden; background: var(--white); }
  body { font-family: "Alegreya Sans", sans-serif; }
  .page { position: relative; width: 928px; height: 1200px; background: var(--white); }

  .top-band {
    position: absolute; left: 0; top: 0; width: 100%; height: 86px;
    background: linear-gradient(to bottom, var(--band-dark) 0%, #2e68a8 30%, #7aa7d6 58%, rgba(255,255,255,0) 100%);
  }

  .section-title {
    position: absolute; left: 94px; font-weight: 400; letter-spacing: -0.5px; line-height: 1;
  }
  .welcome-title { top: 82px; font-size: 80px; color: var(--brand-blue); }
  .aim-title { top: 670px; font-size: 82px; color: var(--brand-grey); }

  .intro-card {
    position: absolute; left: 84px; top: 202px; width: 781px; height: 134px;
    border-radius: 14px; background: var(--white);
    box-shadow: 0 0 7px rgba(80,110,150,0.35);
    color: var(--brand-blue); text-align: center;
    font-size: 17px; line-height: 21px; padding: 18px 40px 0;
  }
  .intro-card p + p { margin-top: 21px; }

  .body-copy {
    position: absolute; left: 94px; top: 388px; width: 763px;
    font-size: 15.6px; line-height: 22.6px; font-weight: 300; color: var(--body-grey);
    text-align: justify;
  }
  .body-copy p + p { margin-top: 22.6px; }

  .aim-lead {
    position: absolute; left: 94px; top: 786px; width: 770px;
    font-size: 16.2px; line-height: 22px; font-weight: 500; color: var(--body-grey);
  }

  .aim-list { position: absolute; left: 104px; top: 856px; width: 760px; list-style: none; }
  .aim-list li {
    position: relative; padding-left: 30px;
    font-size: 15.6px; line-height: 21px; font-weight: 300; color: var(--muted-grey);
    margin-bottom: 23px;
  }
  .aim-list li::before {
    content: ""; position: absolute; left: 0; top: 4px;
    width: 21px; height: 21px; border-radius: 50%; background: var(--bullet-grey);
  }

  .footer-rule { position: absolute; left: 84px; top: 1133px; width: 772px; height: 6px; display: flex; }
  .footer-rule .rule-blue { width: 568px; background: var(--brand-blue); }
  .footer-rule .rule-grey { flex: 1; background: var(--brand-grey); }
</style>
</head>
<body>
<main class="page">
  <div class="top-band"></div>

  <h1 class="section-title welcome-title">Welcome</h1>

  <div class="intro-card">
    <p>Welcome and thanks for choosing Brightfold Web Studio, part of the Brightfold Solutions Group in Tallowbrook.</p>
    <p>In this information booklet you will find information about the design process, our design and editing platform, Pricing and our hosting and domain service.</p>
  </div>

  <div class="body-copy">
    <p>Your standard, successful website is made from a blend of beautiful design, clearly written content and a well-thought-out conversion funnel. And all of that’s great, but who wants to just be ‘standard,’ when you can be so much more? To maximize your website’s potential as a customer-conversion machine, you need to create a visitor experience that is highly engaging and speaks directly to your potential customers’ needs.</p>
    <p>We deliver professional, high-quality websites for our clients that evoke emotion and improve interaction. Simply put, our design work delivers real, measurable results.</p>
    <p>Our state-of-the-art features are proven to increase search engine ranking, boost sales, and deliver a better over-all experience across every device type.</p>
  </div>

  <h2 class="section-title aim-title">Our Aim</h2>

  <p class="aim-lead">We take the hassle out of setting up a website and take care of the website design, domain registration, SEO and hosting. We aim:</p>

  <ul class="aim-list">
    <li>To design a website that the client will love</li>
    <li>To listen to our Clients and ensure that they get the website they want and have it looking exactly how they wish.</li>
    <li>To produce smart looking, visually appealing, high quality website at an affordable price, for your Clients Businesses.</li>
    <li>To produce website without the big price tag</li>
  </ul>

  <div class="footer-rule"><span class="rule-blue"></span><span class="rule-grey"></span></div>
</main>
</body>
</html>
```